Lantern Business Cards

Need business cards for my employees at my restaurant.

Needs to include:
Our Logo
Lantern Forks & Cellar
Name: Miriam Toddwell
Title : Owner
Address: 847 Pickering Ave. Lake Havasu City, AZ 86519
Web: www.lanternkitchenbay.com
Phone: 928-555-0147
Cell: 928-555-0183
Email: info@lanternkitchenbay.com

```html
<!DOCTYPE html>
<html lang="en">
<head>
<meta charset="utf-8">
<title>Lantern Forks &amp; Cellar – Business Cards</title>
<link href="https://fonts.googleapis.com/css2?family=Roboto:wght@400;500;700&display=swap" rel="stylesheet">
<style>
  :root {
    --brand-red: #c4202f;
    --ink: #2b2b2b;
    --black: #0c0c0c;
    --card: #ffffff;
    --backdrop: #ebebeb;
  }
  * { margin: 0; padding: 0; box-sizing: border-box; }
  html, body { width: 1051px; height: 1200px; overflow: hidden; }
  body {
    background: var(--backdrop);
    font-family: "Roboto", Arial, sans-serif;
    color: var(--ink);
    position: relative;
  }
  .card {
    position: absolute;
    width: 798px;
    height: 456px;
    background: var(--card);
    border-radius: 29px;
    overflow: hidden;
  }
  .card-front { left: 130px; top: 117px; }
  .card-back { left: 139px; top: 604px; }

  .brand-mark {
    position: absolute;
    display: flex;
    flex-direction: column;
    align-items: center;
  }
  .brand-dot {
    border-radius: 50%;
    background: var(--brand-red);
    flex: none;
  }
  .brand-name {
    color: var(--brand-red);
    font-weight: 700;
    letter-spacing: 1px;
    line-height: 0.9;
  }
  .brand-tagline {
    width: 100%;
    display: flex;
    align-items: center;
    color: var(--ink);
    font-weight: 400;
    text-transform: uppercase;
    white-space: nowrap;
    line-height: 1;
  }
  .brand-tagline .rule {
    flex: 1;
    height: 1.5px;
    background: var(--ink);
  }

  .card-front .brand-mark { left: 486px; top: 55px; width: 265px; }
  .card-front .brand-dot { width: 96px; height: 96px; margin-bottom: 16px; }
  .card-front .brand-name { font-size: 52px; }
  .card-front .brand-tagline { font-size: 13px; letter-spacing: 1.3px; margin-top: 5px; gap: 12px; }

  .person-name {
    position: absolute;
    left: 33px; top: 243px;
    font-size: 38px;
    font-weight: 700;
    color: var(--brand-red);
    letter-spacing: -0.5px;
  }
  .person-title {
    position: absolute;
    left: 33px; top: 297px;
    font-size: 21px;
    font-weight: 400;
  }
  .divider {
    position: absolute;
    left: 33px; top: 332px;
    width: 733px; height: 1.5px;
    background: var(--ink);
  }
  .contact {
    position: absolute;
    display: flex;
    align-items: center;
    font-size: 20px;
    white-space: nowrap;
  }
  .contact svg { width: 22px; height: 22px; margin-right: 11px; fill: var(--brand-red); flex: none; }
  .phone-office, .phone-cell { letter-spacing: 1px; }
  .phone-office { left: 33px; top: 354px; }
  .phone-cell { left: 33px; top: 391px; }
  .email { left: 226px; top: 354px; }
  .web { left: 226px; top: 391px; }
  .address {
    position: absolute;
    right: 32px; top: 356px;
    text-align: right;
    font-size: 20px;
    line-height: 27px;
    font-style: normal;
  }
  .footer-band {
    position: absolute;
    left: 0; bottom: 0;
    width: 100%; height: 11px;
    display: flex;
  }
  .footer-band .band-red { width: 566px; background: var(--brand-red); }
  .footer-band .band-black { flex: 1; background: var(--black); }

  .card-back .brand-mark { left: 202px; top: 94px; width: 410px; }
  .card-back .brand-dot { width: 160px; height: 160px; margin-bottom: 18px; }
  .card-back .brand-name { font-size: 76px; }
  .card-back .brand-tagline { font-size: 20px; letter-spacing: 2px; margin-top: 8px; gap: 17px; }
  .back-web {
    position: absolute;
    left: 0; width: 100%; top: 396px;
    text-align: center;
    font-size: 21px;
  }
</style>
</head>
<body>
  <section class="card card-front">
    <div class="brand-mark">
      <div class="brand-dot"></div>
      <div class="brand-name">LANTERN</div>
      <div class="brand-tagline"><span class="rule"></span><span>Forks &amp; Cellar</span><span class="rule"></span></div>
    </div>

    <h1 class="person-name">Miriam Toddwell</h1>
    <p class="person-title">Owner</p>
    <div class="divider"></div>

    <div class="contact phone-office">
      <svg viewBox="0 0 24 24" aria-hidden="true"><path d="M6.6 10.8a15.1 15.1 0 0 0 6.6 6.6l2.2-2.2a1 1 0 0 1 1-.25 11.4 11.4 0 0 0 3.6.57 1 1 0 0 1 1 1V20a1 1 0 0 1-1 1A17 17 0 0 1 3 4a1 1 0 0 1 1-1h3.5a1 1 0 0 1 1 1c0 1.25.2 2.45.57 3.570a1 1 0 0 1-.25 1z"/></svg>
      <span>928-555-0147</span>
    </div>
    <div class="contact phone-cell">
      <svg viewBox="0 0 24 24" aria-hidden="true"><path d="M7 1h10a2 2 0 0 1 2 2v18a2 2 0 0 1-2 2H7a2 2 0 0 1-2-2V3a2 2 0 0 1 2-2zm0 3v14h10V4zm5 15.5a1.2 1.2 0 1 0 0 2.4 1.2 1.2 0 0 0 0-2.4z"/></svg>
      <span>928-555-0183</span>
    </div>
    <div class="contact email">
      <svg viewBox="0 0 24 24" aria-hidden="true"><path d="M2 5h20v14H2zm2 2v.5l8 5 8-5V7l-8 5z"/></svg>
      <span>info@lanternkitchenbay.com</span>
    </div>
    <div class="contact web">
      <svg viewBox="0 0 24 24" aria-hidden="true"><path d="M12 2a10 10 0 1 0 0 20 10 10 0 0 0 0-20zm0 2a8 8 0 0 1 6.9 4H15l-1 2-2-1-2 2 1 3h2l1 3-1 3.9A8 8 0 0 1 4.2 10.3L7 12l1-3-2-3A8 8 0 0 1 12 4z"/></svg>
      <span>www.lanternkitchenbay.com</span>
    </div>

    <address class="address">
      847 Pickering Ave. Lake<br>
      Havasu City, AZ 86519
    </address>

    <div class="footer-band">
      <div class="band-red"></div>
      <div class="band-black"></div>
    </div>
  </section>

  <section class="card card-back">
    <div class="brand-mark">
      <div class="brand-dot"></div>
      <div class="brand-name">LANTERN</div>
      <div class="brand-tagline"><span class="rule"></span><span>Forks &amp; Cellar</span><span class="rule"></span></div>
    </div>
    <p class="back-web">www.lanternkitchenbay.com</p>
  </section>
</body>
</html>
```